velumora.eu :: Design ideas (no coding) for key pages of Personalized greeting cards online store

We need your vision on modern, clean, easy to read user interface (UI) for online service of personalized printed products, like greeting cards, postcards, fridge magnets, clips and etc.
Your vision should include UI presentation for:
- Home page with login (including soc nets)
- Product Designer page
- Cart pages (products and address selection)
- Example of general internal page (pricing, terms, etc)
- Artist info and portfolio page
We are looking for ideas we will love, NOT complete design of a whole site.
Top design/vision will we used as a basement for separate contract on complete design of the site.

UI should be based on existing functionality with some extent. It should not break ideas or methods used on prototype but designers are free to offer own product presentations, designer’s layout and cart views.

Prototype:
English: http://velumora.eu
Russian: http://velumora.ru
Lithuanian: http://velumora.lt

Target Market(s)

People of 16-45 y.o. who likes to be distinctive, personal.

Industry/Entity Type

Store

Requirements
Must have
• Your work should meet attached requirements.
Site is multilingual. Wording should assume varieties in length on different languages.
Clean and easy to read UI
Flat design preferrably
Should be based on assets which are free or available for royalty-free licensing
Should not have
• heavy, meaningless 3D and shadow effects
Show NOT copy sites like: kindlow.com, tarnbell.co.uk

```html
<!DOCTYPE html>
<html lang="en">
<head>
<meta charset="utf-8">
<title>velumora – Greeting Cards</title>
<link href="https://fonts.googleapis.com/css2?family=Comfortaa:wght@400;700&family=Ubuntu:wght@400;700&display=swap" rel="stylesheet">
<style>
  :root{
    --bg-top:#f8c98c;
    --bg-bottom:#fdebbd;
    --panel:#fdebc9;
    --ink:#5a1a14;
    --accent:#8e1b12;
    --card-front:#f0f1f0;
    --card-back:#d9dad9;
    --white:#ffffff;
    --plus:#6cc04a;
  }
  *{margin:0;padding:0;box-sizing:border-box}
  html,body{width:1200px;height:660px;overflow:hidden}
  body{
    position:relative;
    font-family:"Comfortaa",sans-serif;
    background:linear-gradient(180deg,var(--bg-top) 0%,var(--bg-bottom) 100%);
    color:var(--ink);
  }
  .abs{position:absolute}

  /* header band */
  .header-band{
    left:6px;top:0;width:1188px;height:90px;
    background:linear-gradient(100deg,#f9d9bd 0%,#dfe0c9 18%,#f8cfae 35%,#fae3c9 50%,#f6cda9 66%,#dcdcc4 82%,#f9d8b8 100%);
    box-shadow:0 2px 4px rgba(120,60,20,.25);
  }
  .brand-mark{left:166px;top:12px;width:44px;height:44px;background:#c8473a}
  .brand-name{left:154px;top:68px;font-size:14px;color:var(--ink)}
  .tagline{left:236px;top:24px;font-size:17.5px;line-height:22px;color:var(--ink);white-space:nowrap}
  .nav-arrow{
    top:49px;width:20px;height:20px;border-radius:50%;
    background:#f2c9a3;color:var(--ink);font-size:15px;line-height:17px;text-align:center;
    font-family:"Ubuntu",sans-serif;font-weight:700;
  }

  /* toolbar */
  .toolbar{
    left:156px;top:88px;width:888px;height:84px;background:var(--panel);
    border-radius:0 0 18px 18px;box-shadow:0 2px 3px rgba(150,90,30,.3);
  }
  .center-tab-top{left:548px;top:26px;width:106px;height:72px;background:var(--panel);border-radius:16px 16px 0 0}
  .center-tab-bottom{
    left:504px;top:88px;width:192px;height:100px;background:var(--panel);
    border-radius:0 0 22px 22px;box-shadow:0 2px 3px rgba(150,90,30,.3);
  }
  .shape-icon{border:2px dashed var(--accent)}
  .label{font-size:11px;color:var(--accent);white-space:nowrap}
  .pill{background:var(--accent);color:var(--white);border-radius:7px;text-align:center;font-size:10.5px;line-height:12px;white-space:nowrap}
  .format{font-size:11px;color:var(--ink);line-height:14.5px}
  .slot-pill{background:var(--accent);color:var(--white);border-radius:6px;font-size:7px;line-height:11px;text-align:center;white-space:nowrap}
  .slot-text{font-size:7.5px;color:var(--accent);white-space:nowrap}
  .swatch{width:26px;height:26px;transform:rotate(45deg);border:2px solid var(--white)}
  .swatch-one{background:linear-gradient(135deg,#fde14b,#f39a1d)}
  .swatch-two{background:#edc7a0;opacity:.8}
  .section-title{left:504px;top:162px;width:192px;text-align:center;font-size:12.5px;color:var(--ink)}
  .gear{left:588px;top:176px;width:24px;height:24px}

  .themes-label{left:712px;top:101px;font-size:10px;color:var(--ink);white-space:nowrap}
  .themes-box{
    left:762px;top:103px;width:266px;height:53px;background:var(--white);
    box-shadow:0 1px 3px rgba(0,0,0,.25);padding:5px 6px;
    font-family:"Ubuntu",sans-serif;font-weight:700;line-height:18px;
  }
  .themes-box span{margin-right:5px;white-space:nowrap}
  .add-theme{left:1018px;top:98px;width:21px;height:21px;border-radius:50%;background:var(--plus);color:var(--white);text-align:center;font:700 18px/21px "Ubuntu",sans-serif}

  /* card grid */
  .card{width:174px}
  .card svg{display:block}
  .card-front{background:var(--card-front);width:174px}
</style>
</head>
<body>

<div class="abs header-band" role="img" aria-label="Faceted triangle pattern in peach and sage tones"></div>
<div class="abs brand-mark"></div>
<div class="abs brand-name">velumora</div>
<div class="abs tagline">The Individual Greeting Cards<br>According To Your Mood</div>

<div class="abs toolbar"></div>
<div class="abs center-tab-bottom"></div>
<div class="abs center-tab-top"></div>

<div class="abs nav-arrow" style="left:510px">«</div>
<div class="abs nav-arrow" style="left:667px">»</div>

<svg class="abs" style="left:583px;top:38px" width="34" height="34" viewBox="0 0 34 34" aria-label="Cards">
  <rect x="3" y="3" width="17" height="22" fill="#8e1b12"/>
  <rect x="10" y="11" width="20" height="20" fill="#a52416" stroke="#fdebc9" stroke-width="2"/>
</svg>

<!-- formats -->
<div class="abs shape-icon" style="left:172px;top:101px;width:54px;height:36px"></div>
<div class="abs label" style="left:171px;top:146px">Landscape</div>
<div class="abs shape-icon" style="left:263px;top:101px;width:24px;height:36px"></div>
<div class="abs pill" style="left:250px;top:145px;width:51px">Portrait</div>
<div class="abs shape-icon" style="left:322px;top:101px;width:36px;height:36px"></div>
<div class="abs label" style="left:323px;top:146px">Square</div>

<div class="abs pill" style="left:388px;top:102px;width:70px">All Formats</div>
<div class="abs format" style="left:393px;top:115px">Standard Cards<br>Mini Card<br>Nano Card</div>

<!-- colours -->
<div class="abs slot-pill" style="left:501px;top:106px;width:48px">color slot 1</div>
<div class="abs swatch swatch-one" style="left:511px;top:125px"></div>
<svg class="abs" style="left:565px;top:86px" width="70" height="70" viewBox="0 0 70 70" aria-label="Colour wheel">
  <circle cx="35" cy="35" r="31" fill="none" stroke="#ddd" stroke-width="7"/>
  <circle cx="35" cy="35" r="31" fill="none" stroke="#e34b3a" stroke-width="7" stroke-dasharray="6 4"/>
  <circle cx="35" cy="35" r="31" fill="none" stroke="#3b8fd6" stroke-width="7" stroke-dasharray="6 54" stroke-dashoffset="10"/>
  <circle cx="35" cy="35" r="31" fill="none" stroke="#6cbf4a" stroke-width="7" stroke-dasharray="6 44" stroke-dashoffset="30"/>
  <circle cx="35" cy="35" r="31" fill="none" stroke="#f3a623" stroke-width="7" stroke-dasharray="6 34" stroke-dashoffset="50"/>
  <circle cx="35" cy="35" r="24" fill="#fff"/>
  <polygon points="35,14 56,35 35,56 14,35" fill="#f5a623" stroke="#fde14b" stroke-width="2"/>
</svg>
<div class="abs section-title">Greeting Cards</div>
<div class="abs slot-text" style="left:655px;top:108px">color slot 2</div>
<div class="abs swatch swatch-two" style="left:663px;top:125px"></div>
<svg class="abs gear" viewBox="0 0 24 24" aria-label="Settings">
  <circle cx="12" cy="12" r="12" fill="#8e1b12"/>
  <circle cx="12" cy="12" r="5.5" fill="none" stroke="#fff" stroke-width="3" stroke-dasharray="3 1.3"/>
  <circle cx="12" cy="12" r="2.5" fill="none" stroke="#fff" stroke-width="1.5"/>
</svg>

<!-- themes -->
<div class="abs themes-label">Themes :</div>
<div class="abs themes-box">
  <span style="color:#a9c6e8;font-size:10px">All</span><span style="color:#e9704a;font-size:6.5px">Roses</span><span style="color:#8bc34a;font-size:8px">Birthday Cards</span><span style="color:#2a6fa8;font-size:8px">Cats</span><span style="color:#f2a21c;font-size:12px">Congratulations !</span><br>
  <span style="color:#e2506b;font-size:8px">Dogs</span><span style="color:#2a6fa8;font-size:6.5px">Flowers</span><span style="color:#7cbf4a;font-size:11px">For children</span><span style="color:#d9461e;font-size:5px">Friendship</span><span style="color:#f29bb0;font-size:9px">Love</span>
</div>
<div class="abs add-theme">+</div>

<!-- cards -->
<div class="abs card" style="left:156px;top:212px">
  <svg width="174" height="12"><polygon points="0,12 160,0 160,12" fill="var(--card-back)"/></svg>
  <div class="card-front" style="height:262px"></div>
</div>
<div class="abs card" style="left:388px;top:212px">
  <svg width="174" height="12"><polygon points="0,12 160,0 160,12" fill="var(--card-back)"/></svg>
  <div class="card-front" style="height:174px"></div>
</div>
<div class="abs card" style="left:620px;top:212px">
  <svg width="174" height="12"><polygon points="0,12 160,0 160,12" fill="var(--card-back)"/></svg>
  <div class="card-front" style="height:262px"></div>
</div>
<div class="abs card" style="left:853px;top:212px">
  <svg width="174" height="12"><polygon points="0,12 160,0 160,12" fill="var(--card-back)"/></svg>
  <div class="card-front" style="height:174px"></div>
</div>
<div class="abs card" style="left:383px;top:432px">
  <svg width="174" height="12"><polygon points="0,12 160,0 160,12" fill="var(--card-back)"/></svg>
  <div class="card-front" style="height:230px"></div>
</div>
<div class="abs card" style="left:853px;top:432px">
  <svg width="174" height="12"><polygon points="0,12 160,0 160,12" fill="var(--card-back)"/></svg>
  <div class="card-front" style="height:230px"></div>
</div>
<div class="abs card" style="left:149px;top:518px">
  <svg width="174" height="12"><polygon points="0,12 160,0 160,12" fill="var(--card-back)"/></svg>
  <div class="card-front" style="height:150px"></div>
</div>
<div class="abs card" style="left:618px;top:518px">
  <svg width="174" height="12"><polygon points="0,12 160,0 160,12" fill="var(--card-back)"/></svg>
  <div class="card-front" style="height:150px"></div>
</div>

</body>
</html>
```